Book Cover Design Project

A non-fiction book on child protection, specifically... keeping young children safe from predators and keeping teenagers safe from themselves.

Title:
Beneath Our Roof

Subtitle:
A Guide To Keeping Your Children Safe

Author:
Martin Kellaway

```html
<!DOCTYPE html>
<html lang="en">
<head>
<meta charset="utf-8">
<title>Beneath Our Roof — Book Cover</title>
<link rel="stylesheet" href="https://fonts.googleapis.com/css2?family=Anton&display=swap">
<style>
  :root {
    --sky-blue: #00aeef;
    --paper: #ffffff;
    --page-bg: #ffffff;
    --photo-warm: #f3c9b4;
    --photo-pink: #ef9fc0;
    --photo-red: #e0433a;
    --photo-orange: #f5752a;
    --photo-aqua: #cdeef2;
  }
  html, body {
    margin: 0;
    padding: 0;
    width: 1000px;
    height: 1200px;
    overflow: hidden;
    background: var(--page-bg);
  }
  .cover {
    position: absolute;
    left: 157px;
    top: 52px;
    width: 715px;
    height: 1075px;
    background: var(--paper);
    font-family: "Anton", Impact, sans-serif;
  }
  .author-band {
    position: absolute;
    left: 0;
    top: 0;
    width: 100%;
    height: 116px;
    background: var(--sky-blue);
    display: flex;
    align-items: center;
    justify-content: center;
  }
  .author-name {
    margin: 0;
    color: var(--paper);
    font-size: 58px;
    font-weight: 400;
    letter-spacing: 0.2em;
    line-height: 1;
    white-space: nowrap;
  }
  .cover-photo {
    position: absolute;
    left: 0;
    top: 205px;
    width: 100%;
    height: 375px;
    background:
      radial-gradient(ellipse 18% 30% at 12% 35%, var(--photo-warm), transparent 70%),
      radial-gradient(ellipse 18% 30% at 38% 30%, var(--photo-warm), transparent 70%),
      radial-gradient(ellipse 16% 28% at 63% 42%, var(--photo-warm), transparent 70%),
      radial-gradient(ellipse 16% 28% at 88% 36%, var(--photo-warm), transparent 70%),
      linear-gradient(90deg, var(--photo-red) 0%, var(--photo-pink) 35%, var(--photo-aqua) 62%, var(--photo-orange) 100%);
    opacity: 0.85;
  }
  .title {
    position: absolute;
    right: 27px;
    top: 590px;
    margin: 0;
    text-align: right;
    color: var(--sky-blue);
    font-weight: 400;
    line-height: 0.98;
    text-shadow: 0 2px 2px rgba(0, 80, 120, 0.25);
  }
  .title-top {
    display: block;
    font-size: 168px;
    letter-spacing: 0.01em;
  }
  .title-bottom {
    display: block;
    font-size: 150px;
  }
  .subtitle-band {
    position: absolute;
    left: 0;
    bottom: 0;
    width: 100%;
    height: 134px;
    background: var(--sky-blue);
  }
  .subtitle {
    position: absolute;
    right: 55px;
    top: 14px;
    margin: 0;
    color: var(--paper);
    font-size: 44px;
    font-weight: 400;
    line-height: 1.2;
    text-align: right;
  }
</style>
</head>
<body>
  <main class="cover">
    <header class="author-band">
      <p class="author-name">Martin Kellaway</p>
    </header>
    <div class="cover-photo" role="img" aria-label="Photograph of four smiling children lying side by side, chins resting on their hands"></div>
    <h1 class="title">
      <span class="title-top">BENEATH</span>
      <span class="title-bottom">Our Roof</span>
    </h1>
    <footer class="subtitle-band">
      <p class="subtitle">A Guide To Keeping Your<br>Children Safe</p>
    </footer>
  </main>
</body>
</html>
```